2020 Fiber Internet Service Now Available

We want a design a one-sided 8.5x11 FLYER (3 colors) and in PORTRAIT that we can fold ourselves and stuff into a 9-1/2" x 4-1/8" envelope. We want to have a modifiable text box in selected areas of the brochure (with matching font) that we can insert more specialized text/content on an as-needed basis. We would like the delivery of a template we can print from a pdf or Google Docs. The smallest margins possible are appreciated. We do not expect full bleed artwork. If a custom font is used, we want that to be delivered as well so that we can install it on a Windows 10 machine.

The goal of the message is that we are advising the recipient of this flyer that fiber-optic internet service is available at their home or business.

We want possibly some catchy graphics on the brochure. We do not want this to look like 'junk mail'. This needs to be very professional and clean and catchy but not to lose the authenticity of our small, locally-owned business. We are a small fiber optic ISP, competing with the 'big boys' such as Telvora, Brisket and QN&P. We offer the fastest speeds available in these areas that we are investing in. Our plan is to send these to all addresses along a construction route either before or during the construction phase. You can look at our web site at www.klmesh.example. Be sure to click on the Updates menu item as it shows some of our construction projects that we are targeting. It just gives you an idea of what we are accomplishing here in our city. Google reviews and facebook page. https://www.searchly.example/search?q=kl+mesh&oq=kl+mesh https://www.socialpage.example/HollowmereNetworks/

PLEASE NOTE: I ATTACHED HI-RES LOGO GRAPHICS IN THE ZIP FILE. HOWEVER (AND DESPITE THE FACT THAT THE ENVELOPE CURRENTLY HAS IT ON IT) WE ARE MOVING AWAY FROM THE "Wired for you" wording along with removing the green house outline. I attached another png that shows what I'm talking about. The hi-res EPS file should help to allow you to eliminate the unneeded portion of the logo.

As a follow up, we will most likely hire the same designer to do an 3-color envelope design as well that will fit the brochures.

When it comes time for that project, we will be using envelopes that we already had printed with two colors (blue and black). I have attached a photo of the envelope that I took with my phone. Unfortunately, I do not have a design file for this. But, just know that we'll be printing this design on these same envelopes that already have this on it!

Target Market(s)

homes and businesses along a fiber optic construction route

Industry/Entity Type

Internet Service Provider

Requirements
Must have
• For colors, use the colors that are in our logo (attached). one-sided 8.5x11 FLYER (3 colors) and in PORTRAIT
Nice to have
• try not to just copy our web site content.
Should not have
• absolutely no junk mail buzz words. needs to be authentic.

```html
<!DOCTYPE html>
<html lang="en">
<head>
<meta charset="utf-8">
<title>KL Mesh Flyer</title>
<link rel="stylesheet" href="https://fonts.googleapis.com/css2?family=Exo+2:wght@700&family=Ubuntu:wght@400&display=swap">
<style>
  :root {
    --backdrop: #3340a8;
    --sky-top: #4150bf;
    --sky-bottom: #5a6bd0;
    --paper: #dcdcdc;
    --card: #e4e4e4;
    --heading-blue: #2e3fb5;
    --accent-gold: #d99d3e;
    --body-ink: #2f2f2f;
    --white: #ffffff;
  }
  * { margin: 0; padding: 0; box-sizing: border-box; }
  html, body { width: 1200px; height: 855px; overflow: hidden; }
  body {
    background: var(--backdrop);
    font-family: "Ubuntu", Arial, sans-serif;
    position: relative;
  }
  .flyer {
    position: absolute;
    left: 300px; top: 18px;
    width: 600px; height: 819px;
    background: var(--paper);
    overflow: hidden;
  }
  .hero-art {
    position: absolute; left: 0; top: 0;
    width: 600px; height: 320px;
    background: linear-gradient(180deg, var(--sky-top) 0%, var(--sky-bottom) 78%, var(--paper) 100%);
  }
  .brand {
    position: absolute; left: 26px; top: 140px;
    color: var(--white);
    font-family: "Exo 2", Arial, sans-serif;
    font-weight: 700;
  }
  .brand-name { font-size: 44px; line-height: 1; letter-spacing: 1px; }
  .card {
    position: absolute;
    background: var(--card);
    border-radius: 26px;
    box-shadow: 3px 4px 8px rgba(0,0,0,0.28);
    color: var(--body-ink);
  }
  .card-head { display: flex; align-items: center; gap: 10px; }
  .icon-badge {
    flex: none;
    border-radius: 50%;
    background: var(--accent-gold);
    display: flex; align-items: center; justify-content: center;
  }
  .card-title {
    font-family: "Exo 2", Arial, sans-serif;
    font-weight: 700;
    color: var(--heading-blue);
    line-height: 1.05;
  }
  .intro-card { width: 178px; height: 218px; padding: 12px 14px; }
  .intro-card .icon-badge { width: 30px; height: 30px; }
  .intro-card .card-title { font-size: 17px; text-transform: uppercase; }
  .intro-card p { font-size: 9.6px; line-height: 1.32; margin-top: 8px; }
  .about-card { left: 87px; top: 347px; }
  .team-card { left: 330px; top: 347px; }
  .offer-heading {
    position: absolute; left: 220px; top: 598px;
    display: flex; align-items: center; gap: 6px;
  }
  .offer-heading .mini-art {
    width: 20px; height: 30px;
    border-radius: 10px 10px 4px 4px;
    background: linear-gradient(180deg, var(--white), var(--accent-gold));
  }
  .offer-heading h2 {
    font-family: "Exo 2", Arial, sans-serif; font-weight: 700;
    color: var(--heading-blue); font-size: 17px; text-transform: uppercase;
  }
  .offer-card { width: 130px; height: 162px; padding: 10px 9px; top: 646px; }
  .offer-card .card-head { gap: 6px; min-height: 26px; }
  .offer-card .icon-badge { width: 22px; height: 22px; }
  .offer-card .card-title { font-size: 10px; }
  .offer-card.fiber .card-title { font-size: 12.5px; }
  .offer-card p { font-size: 6.6px; line-height: 1.28; margin-top: 6px; }
  .offer-card.fiber { left: 87px; }
  .offer-card.wireless { left: 250px; }
  .offer-card.voip { left: 413px; }
</style>
</head>
<body>
  <main class="flyer">
    <div class="hero-art" role="img" aria-label="Illustration of a white and gold rocket launching among line-drawn planets above soft clouds"></div>

    <div class="brand">
      <div class="brand-name">KL MESH</div>
    </div>

    <section class="card intro-card about-card">
      <div class="card-head">
        <span class="icon-badge">
          <svg width="16" height="16" viewBox="0 0 16 16" aria-hidden="true"><rect x="2" y="8" width="3" height="6" fill="#fff"/><rect x="6.5" y="5" width="3" height="9" fill="#fff"/><rect x="11" y="2" width="3" height="12" fill="#fff"/></svg>
        </span>
        <h2 class="card-title">About Us</h2>
      </div>
      <p>After years of trying (and failing) to get the big companies to bring decent internet service to our area, Owen Marsh decided it was time to solve the problem himself. In 2012, he founded Hollowmere Networks with the goal of offering high speed, unlimited internet service to families in Brackton that had been ignored by other providers.</p>
    </section>

    <section class="card intro-card team-card">
      <div class="card-head">
        <span class="icon-badge">
          <svg width="16" height="16" viewBox="0 0 16 16" aria-hidden="true"><circle cx="8" cy="8" r="5" fill="none" stroke="#fff" stroke-width="3" stroke-dasharray="2.2 1.4"/><circle cx="8" cy="8" r="2" fill="#fff"/></svg>
        </span>
        <h2 class="card-title">Our Team</h2>
      </div>
      <p>Together with their team, Owen and Clara Marsh are working to extend the KL Mesh network into more areas around Brackton. With a firm dedication to reliability, friendly service, and complete customer satisfaction, Hollowmere Networks strives to be the preferred internet service provider in the greater Brackton area.</p>
    </section>

    <div class="offer-heading">
      <span class="mini-art" role="img" aria-label="Small rocket illustration"></span>
      <h2>What We Offer</h2>
    </div>

    <section class="card offer-card fiber">
      <div class="card-head">
        <span class="icon-badge">
          <svg width="12" height="12" viewBox="0 0 12 12" aria-hidden="true"><path d="M1 6 L6 1.5 L11 6 H9.5 V10.5 H2.5 V6 Z" fill="#fff"/></svg>
        </span>
        <h3 class="card-title">KL Mesh</h3>
      </div>
      <p>High speed, Fiber to the Premise internet service that is fully scalable to meet your internet needs for years to come! With plans starting at 50x50 Mbps for $79.99/mo ($39.99/mo in town and some planned communities), KL Mesh will provide fast, reliable internet service to your home or business. All plans offer completely unlimited data.</p>
    </section>

    <section class="card offer-card wireless">
      <div class="card-head">
        <span class="icon-badge">
          <svg width="12" height="12" viewBox="0 0 12 12" aria-hidden="true"><g fill="none" stroke="#fff" stroke-width="1.3" stroke-linecap="round"><path d="M1.5 5 A6.5 6.5 0 0 1 10.5 5"/><path d="M3.3 7 A4 4 0 0 1 8.7 7"/></g><circle cx="6" cy="9.4" r="1.1" fill="#fff"/></svg>
        </span>
        <h3 class="card-title">Fixed Wireless<br>Internet Service</h3>
      </div>
      <p>Fixed wireless service reaches homes and businesses beyond our fiber lines. Our local towers deliver steady, low-latency connections with unlimited data and no contracts, installed and supported by our own Brackton team. It is a dependable option while fiber construction reaches your street, and a great fit for rural properties.</p>
    </section>

    <section class="card offer-card voip">
      <div class="card-head">
        <span class="icon-badge">
          <svg width="12" height="12" viewBox="0 0 12 12" aria-hidden="true"><path d="M2.5 1.5 L4.5 1.2 L5.4 3.8 L4.2 4.8 A6 6 0 0 0 7.2 7.8 L8.2 6.6 L10.8 7.5 L10.5 9.5 A1.5 1.5 0 0 1 9 10.8 A8.5 8.5 0 0 1 1.2 3 A1.5 1.5 0 0 1 2.5 1.5 Z" fill="#fff"/></svg>
        </span>
        <h3 class="card-title">VoIP Phone<br>Service</h3>
      </div>
      <p>Keep your current number and make crystal-clear calls over your KL Mesh connection. Home and business phone plans include unlimited local and long distance calling, voicemail, caller ID and call forwarding. Our team handles the number transfer and setup, so switching is simple, and local help is always a phone call away.</p>
    </section>
  </main>
</body>
</html>
```